Luxury Eco accommodation needs new website

Luxury lodge accommodation on exclusive private property in Flinders Ranges South Australia.
Brand new venture needs new site.
Focus on small group accommodation on exclusive property with outdoor experiences. Mountain biking , bush walking, outdoor dining.
We currently have a website but are having trouble making it our own. Needs to be "polished" by a professional.
Can you help?

www.tallowridgehomestead.com.au

Target Market(s)

High income travellers, luxury accommodation

Industry/Entity Type

Accommodation

```html
<!DOCTYPE html>
<html lang="en">
<head>
<meta charset="utf-8">
<title>Tallow Ridge Homestead</title>
<link rel="stylesheet" href="https://fonts.googleapis.com/css2?family=Glegoo:wght@400;700&family=Great+Vibes&display=swap">
<style>
:root{
  --ink:#3a2e28;
  --muted:#5a4d45;
  --line:#c9c2bc;
  --rust-dark:#7a4210;
  --tab:#fbf3ee;
  --white:#ffffff;
  --panel:#d9ad78;
  --panel-ink:#3b2a1a;
  --logo:#6e625a;
  --hero-sky:#a9c0d2;
  --hero-warm:#cf7a30;
  --hero-deep:#3e5878;
}
*{margin:0;padding:0;box-sizing:border-box}
html,body{width:1200px;height:878px;overflow:hidden;background:var(--white)}
body{position:relative;font-family:"Glegoo",Georgia,serif;color:var(--ink)}

.site-header{position:absolute;left:0;top:0;width:1200px;height:112px;background:var(--white);border-bottom:2px solid #eee}
.brand{position:absolute;left:158px;top:0;width:146px;height:112px;border:1px solid #ddd;border-top:none;background:var(--white);box-shadow:0 1px 3px rgba(0,0,0,.12);display:flex;flex-direction:column;align-items:center;justify-content:center;gap:10px}
.brand-mark{width:40px;height:40px;background:var(--logo)}
.brand-name{font-size:14px;color:var(--logo);text-align:center;line-height:1.15;letter-spacing:1px;text-transform:uppercase}

.main-nav{position:absolute;left:0;top:0;width:1200px;height:112px}
.main-nav a{position:absolute;top:35px;height:44px;line-height:46px;font-size:16px;color:var(--ink);text-decoration:none;text-transform:uppercase;white-space:nowrap}
.main-nav a.active{left:392px;width:163px;text-align:center;background:var(--tab);border-top:2px solid #eedcd0;border-radius:3px;box-shadow:0 2px 3px rgba(0,0,0,.06)}
.main-nav .nav-stays{left:576px}
.main-nav .nav-experiences{left:715px}
.main-nav .nav-gallery{left:861px}
.main-nav .nav-contact{left:968px}

.hero{position:absolute;left:0;top:112px;width:1200px;height:535px;
  background:linear-gradient(180deg,var(--hero-sky) 0%,var(--hero-warm) 35%,#b65a22 62%,var(--hero-deep) 100%)}
.hero-quote{position:absolute;left:132px;top:448px;font-family:"Great Vibes",cursive;font-size:29px;line-height:33px;color:var(--white);text-shadow:1px 1px 2px rgba(0,0,0,.7)}
.booking-panel{position:absolute;left:876px;top:434px;width:264px;height:112px;transform:rotate(-3deg);background:var(--panel);border-radius:3px;box-shadow:2px 3px 5px rgba(0,0,0,.3);text-align:center;padding-top:14px;color:var(--panel-ink)}
.booking-panel .panel-title{font-size:14px;text-transform:uppercase;letter-spacing:.3px}
.booking-panel .panel-line{font-size:13.5px;margin-top:8px}
.booking-panel .panel-email{font-size:13px}

.slider-dots{position:absolute;left:543px;top:631px;width:108px;height:31px;background:var(--white);border-radius:16px;box-shadow:0 3px 5px rgba(0,0,0,.2);display:flex;justify-content:center;align-items:center;gap:9px}
.slider-dots span{width:14px;height:14px;border-radius:50%;background:#e4e4e4;box-shadow:inset 0 1px 2px rgba(0,0,0,.3)}
.slider-dots span.current{background:#cfcfcf}

.welcome{position:absolute;left:114px;top:684px;width:958px;text-align:center}
.welcome-title{display:flex;align-items:center;gap:14px;font-size:19.5px;font-weight:400;line-height:26px;color:var(--ink);letter-spacing:.4px}
.welcome-title::before,.welcome-title::after{content:"";flex:1;height:1px;background:var(--line)}
.welcome-text{margin-top:2px;font-size:15px;line-height:21px;color:var(--ink);letter-spacing:.1px}
.btn-more{display:inline-block;margin-top:12px;width:57px;height:26px;line-height:28px;background:linear-gradient(#a8621f,var(--rust-dark));color:var(--white);font-size:15px;text-decoration:none;border-radius:1px}

.site-footer{position:absolute;left:0;top:840px;width:1200px;height:24px;font-size:13px;color:var(--muted)}
.copyright{position:absolute;left:478px;top:4px}
.follow{position:absolute;left:788px;top:4px}
.social{position:absolute;left:859px;top:0;display:flex;gap:5px}
.social a{display:block;width:24px;height:24px;border-radius:4px;background:linear-gradient(#e7a55a,#c0722a);box-shadow:0 1px 2px rgba(0,0,0,.35)}
</style>
</head>
<body>
<header class="site-header">
  <div class="brand">
    <div class="brand-mark"></div>
    <div class="brand-name">Tallow Ridge<br>Homestead</div>
  </div>
  <nav class="main-nav">
    <a class="active" href="#">Luxury Lodge</a>
    <a class="nav-stays" href="#">Other Stays</a>
    <a class="nav-experiences" href="#">Experiences</a>
    <a class="nav-gallery" href="#">Gallery</a>
    <a class="nav-contact" href="#">Contact Us</a>
  </nav>
</header>

<section class="hero" role="img" aria-label="Photograph of red Flinders Ranges mountains at sunset reflected in a still waterhole, with a wooden signpost"></section>
<p class="hero-quote">“ The bones of the earth laid bare.”<br>– Sir Edwin Marlow</p>
<div class="booking-panel">
  <p class="panel-title">For Bookings &amp; Information:</p>
  <p class="panel-line">(08) 8555 0142</p>
  <p class="panel-line panel-email">stay@tallowridgehomestead.com.au</p>
</div>

<div class="slider-dots"><span class="current"></span><span></span><span></span><span></span></div>

<section class="welcome">
  <h1 class="welcome-title">Welcome to our site</h1>
  <p class="welcome-text">Tallow Ridge Lodge is nestled in the heart of SA’s magnificent Flinders Ranges. It is located on Tallow Ridge Homestead, 480 kms north of Adelaide and stretches along the northern boundary of the great Flinders Ranges National Park. The Lodge is tucked into a ridge top near the homestead and overlooks a valley of river red gums and native pines.</p>
  <a class="btn-more" href="#">More</a>
</section>

<footer class="site-footer">
  <span class="copyright">Copyright@2013, Tallow Ridge Homestead</span>
  <span class="follow">Follow Us :</span>
  <div class="social"><a href="#" aria-label="Social page one"></a><a href="#" aria-label="Social page two"></a></div>
</footer>
</body>
</html>
```